Brennick Capital Business Cards

These are professional business cards that are for my family office.
Put fake emails and phone numbers as of now until I finalize those components. This family office controls my families investments, assets, and future. The cards should be professional.
..
.
.
.
I just uploaded another variation of a logo I would like to see as a business card to I am inbeteen which logo to use

Target Market(s)

business

Industry/Entity Type

business

Contact Information for Business Card

Professional, wealth related, finance related.

Requirements
Must have
• Logo

```html
<!DOCTYPE html>
<html lang="en">
<head>
<meta charset="utf-8">
<title>Brennick Capital Business Cards</title>
<link rel="stylesheet" href="https://fonts.googleapis.com/css2?family=Cinzel:wght@500&family=Montserrat:wght@400;600&display=swap">
<style>
  :root {
    --backdrop: #e7e4df;
    --card: #1a1f2b;
    --card-accent: #283042;
    --card-accent-deep: #1f2533;
    --white: #ffffff;
    --grey: #a3a3a3;
    --text-light: #e9e9ec;
  }
  * { margin: 0; padding: 0; box-sizing: border-box; }
  html, body {
    width: 900px; height: 1200px; overflow: hidden;
    background: var(--backdrop);
  }
  .canvas { position: relative; width: 900px; height: 1200px; }
  .card {
    position: absolute;
    background: var(--card);
    border-radius: 28px;
    overflow: hidden;
    box-shadow: 0 10px 24px rgba(0,0,0,0.25);
  }
  .card-front { left: 80px; top: 131px; width: 742px; height: 441px; }
  .card-back  { left: 78px; top: 638px; width: 744px; height: 440px; }

  .wordmark {
    font-family: "Cinzel", serif;
    font-weight: 500;
    color: var(--white);
    letter-spacing: 0.5px;
    white-space: nowrap;
  }
  .card-front .wordmark { position: absolute; left: 36px; top: 66px; font-size: 32px; }

  /* large decorative disc on the front, right side */
  .front-disc {
    position: absolute; left: 445px; top: -8px;
    width: 456px; height: 456px; border-radius: 50%;
    background: radial-gradient(circle at 40% 45%, var(--card-accent) 0%, var(--card-accent-deep) 100%);
    box-shadow: -12px 0 30px rgba(0,0,0,0.25);
  }

  .holder { position: absolute; left: 37px; top: 186px; font-family: "Montserrat", sans-serif; }
  .holder-name { font-size: 25px; font-weight: 600; color: var(--grey); line-height: 1.2; }
  .holder-role { font-size: 15px; color: var(--text-light); margin-top: 2px; }

  .address {
    position: absolute; left: 38px; top: 269px;
    font-family: "Montserrat", sans-serif; font-style: normal;
    font-size: 15.5px; line-height: 21px;
    color: var(--text-light);
  }
  .contacts {
    position: absolute; left: 37px; top: 326px; list-style: none;
    font-family: "Montserrat", sans-serif; font-size: 15.5px; color: var(--text-light);
  }
  .contacts li { display: flex; align-items: center; height: 28.5px; }
  .contacts svg { width: 15px; height: 15px; margin-right: 10px; fill: var(--grey); }

  /* back: one plain circle above the company name */
  .back-mark {
    position: absolute; left: 302px; top: 92px;
    width: 140px; height: 140px; border-radius: 50%;
    background: radial-gradient(circle at 38% 35%, #c4c4c4 0%, var(--grey) 70%, #8c8c8c 100%);
    box-shadow: 0 6px 18px rgba(0,0,0,0.35);
  }
  .card-back .wordmark {
    position: absolute; left: 0; right: 0; top: 318px;
    text-align: center; font-size: 42px;
  }
</style>
</head>
<body>
<main class="canvas">
  <section class="card card-front">
    <div class="front-disc"></div>
    <div class="wordmark">Brennick Capital</div>
    <div class="holder">
      <div class="holder-name">Marcus Ellery</div>
      <div class="holder-role">Owner</div>
    </div>
    <address class="address">
      482 Linden Court Plaza<br>
      Harwell, NJ 07841 USA
    </address>
    <ul class="contacts">
      <li>
        <svg viewBox="0 0 24 24"><path d="M6.6 10.8a15.1 15.1 0 0 0 6.6 6.6l2.2-2.2a1 1 0 0 1 1-.25 11.4 11.4 0 0 0 3.6.57 1 1 0 0 1 1 1V20a1 1 0 0 1-1 1A17 17 0 0 1 3 4a1 1 0 0 1 1-1h3.5a1 1 0 0 1 1 1c0 1.25.2 2.45.57 3.57a1 1 0 0 1-.25 1z"/></svg>
        (555)214-7730
      </li>
      <li>
        <svg viewBox="0 0 24 24"><path d="M2 5h20v2l-10 6L2 7z M2 9l10 6 10-6v10H2z"/></svg>
        info@brennickcapital.com
      </li>
      <li>
        <svg viewBox="0 0 24 24"><path d="M12 2a10 10 0 1 0 0 20 10 10 0 0 0 0-20zm6.9 6h-3a15.6 15.6 0 0 0-1.3-4.1A8 8 0 0 1 18.9 8zM12 4.1c.8 1.1 1.5 2.4 1.9 3.9h-3.8c.4-1.5 1.1-2.8 1.9-3.9zM4.3 14a8 8 0 0 1 0-4h3.4a16 16 0 0 0 0 4zm.8 2h3a15.6 15.6 0 0 0 1.3 4.1A8 8 0 0 1 5.1 16zm3-8h-3a8 8 0 0 1 4.3-4.1A15.6 15.6 0 0 0 8.1 8zM12 19.9c-.8-1.1-1.5-2.4-1.9-3.9h3.8c-.4 1.5-1.1 2.8-1.9 3.9zM14.3 14H9.7a14.7 14.7 0 0 1 0-4h4.6a14.7 14.7 0 0 1 0 4zm.3 6.1A15.6 15.6 0 0 0 15.9 16h3a8 8 0 0 1-4.3 4.1zM16.3 14a16 16 0 0 0 0-4h3.4a8 8 0 0 1 0 4z"/></svg>
        www.brennickcapital.com
      </li>
    </ul>
  </section>

  <section class="card card-back">
    <div class="back-mark"></div>
    <div class="wordmark">Brennick Capital</div>
  </section>
</main>
</body>
</html>
```